Business Card Design Project

We need a business card design for a management consultancy focused on financial innovation and digital money, run by experts from the Financial Services, Telecoms and Money Transfer industries.
Our products include services such as Mobile Payments, Mobile Money, Digital Wallets, Online Payments, Branchless Banking and more. We work with regulatory information, business plans, financial modelling, strategic planning, new products functional specification, new technologies evaluation, etc.
See company logo attached.
We would like to see 2 versions: one in portuguese and one in english (regarding data information). You can see below information needed (whenever there is a difference between the two versions, the first one is in english and the second one in portuguese).

Name
Position
Phone/ Tel: ++55-11-xxxx-xxxx
Cell/ Cel: ++55-11-9 xxxx-xxxx
Dr. Olavo Brendim Av., 312 - Tower II - 16th floor / Avenida Dr. Olavo Brendim, 312 - Torre II - 16o. andar
São Paulo - SP
06217-318 - Brazil/ 06217-318 - Brasil

Reason: 5 days to receive designs.

Target Market(s)

Audience: C-level executives from banks, credit card companies, acquirers, IT developers, retailers

Industry/Entity Type

Financial

Requirements
Must have
• Must use the logo and information above. Front must have white background. Back side should have only logo.
Nice to have
• Back should be in another colour but if it seems too exxagerated, maintain back in white also.
Should not have
• Do not add other illustrations to the business card.

```html
<!DOCTYPE html>
<html lang="en">
<head>
<meta charset="utf-8">
<title>R Castellan Management Consulting – Business Cards</title>
<link rel="stylesheet" href="https://fonts.googleapis.com/css2?family=Cinzel:wght@500&family=Tinos:wght@400;700&display=swap">
<style>
  :root {
    --stage: #e9e7e3;
    --card-white: #ffffff;
    --card-black: #121212;
    --card-black-edge: #1d1d1f;
    --navy: #1f2f63;
    --navy-light: #6f80b8;
    --ink: #222222;
    --mark-faint: #e6e6e8;
    --band: #0b0b0b;
  }
  * { box-sizing: border-box; margin: 0; padding: 0; }
  html, body {
    width: 1200px; height: 784px; overflow: hidden;
    background: var(--stage);
  }
  .canvas {
    position: relative; width: 1200px; height: 784px;
    display: flex; align-items: center; justify-content: center; gap: 48px;
  }
  .card {
    position: relative; width: 540px; height: 310px; overflow: hidden;
    box-shadow: 0 10px 28px rgba(0,0,0,.18);
  }
  .card--back {
    background: radial-gradient(ellipse at 50% 40%, var(--card-black-edge), var(--card-black) 70%);
    display: flex; align-items: center; justify-content: center;
  }
  .brand {
    display: flex; align-items: center; gap: 12px;
    font-family: "Cinzel", serif; font-weight: 500; color: var(--navy);
  }
  .brand__square { width: 34px; height: 34px; background: currentColor; flex: none; }
  .brand__name { font-size: 27px; line-height: 1; letter-spacing: .5px; }
  .brand__sub { display: block; font-size: 13.5px; letter-spacing: .6px; margin-top: 3px; }
  .card--back .brand { color: var(--navy-light); }

  .card--front { background: var(--card-white); }
  .card--front .brand { position: absolute; left: 36px; top: 50px; }
  .front-mark {
    position: absolute; right: 34px; top: 96px; width: 120px; height: 120px;
    background: var(--mark-faint);
  }
  .contact {
    position: absolute; left: 36px; top: 156px;
    font-family: "Tinos", serif; color: var(--ink);
  }
  .contact__name { font-size: 17px; color: var(--navy); }
  .contact__role { font-size: 11.5px; margin-top: 4px; }
  .contact__list { list-style: none; margin-top: 12px; font-size: 11.5px; line-height: 15px; }
  .contact__list li { display: flex; align-items: flex-start; gap: 6px; }
  .contact__list svg { width: 11px; height: 11px; margin-top: 2px; flex: none; fill: var(--ink); }
  .contact__list .indent { padding-left: 17px; }
  .band {
    position: absolute; left: 270px; right: 0; bottom: 12px; height: 30px;
    background: var(--band);
  }
  .rule {
    position: absolute; left: 0; right: 0; bottom: 8px; height: 3px; background: var(--navy);
  }
</style>
</head>
<body>
<main class="canvas">
  <section class="card card--back" aria-label="Card back">
    <div class="brand">
      <span class="brand__square"></span>
      <span class="brand__name">R Castellan<span class="brand__sub">Management Consulting</span></span>
    </div>
  </section>

  <section class="card card--front" aria-label="Card front">
    <div class="brand">
      <span class="brand__square"></span>
      <span class="brand__name">R Castellan<span class="brand__sub">Management Consulting</span></span>
    </div>
    <div class="front-mark"></div>
    <div class="contact">
      <p class="contact__name">Dr. Olavo Brendim</p>
      <p class="contact__role">Founder and Managing Partner</p>
      <ul class="contact__list">
        <li><svg viewBox="0 0 12 12"><path d="M2 1l2 0 1 3-1.3 1a6 6 0 0 0 3.3 3.3L8 7l3 1v2l-1 1C5 11 1 7 1 2z"/></svg>++55-11-xxxx-xxxx</li>
        <li><svg viewBox="0 0 12 12"><path d="M3 0h6v12H3zM4 1.5v7.5h4V1.5z"/></svg>++55-11-9 xxxx-xxxx</li>
        <li><svg viewBox="0 0 12 12"><path d="M0 2h12v8H0zM1 3l5 4 5-4v-.2H1z"/></svg>email@rcastellan.com</li>
        <li><svg viewBox="0 0 12 12"><path d="M6 0l6 5.5h-2V12H7.5V8h-3v4H2V5.5H0z"/></svg>Rua das Acácias, 58 - Suite 1204</li>
        <li class="indent">/ Rua das Acácias, 58 - Sala 1204</li>
      </ul>
    </div>
    <div class="band"></div>
    <div class="rule"></div>
  </section>
</main>
</body>
</html>
```